Brightwave Business Card

Professional Business Card Design required using the attached contact information.

Contact information can be rearranged as required.

The company is a new start up venture developing solar systems, the branding should be in keeping with that of one of the investors whose website is as follows https://www.quorvex.com/

```html
<!DOCTYPE html>
<html lang="en">
<head>
<meta charset="utf-8">
<title>Brightwave – Business Card</title>
<link href="https://fonts.googleapis.com/css2?family=Roboto:wght@400;500&display=swap" rel="stylesheet">
<style>
  :root {
    --page-bg: #161616;
    --card-bg: #262626;
    --card-edge: #303030;
    --logo-silver: #b9b9b9;
    --text-white: #f2f2f2;
    --accent-blue: #3f9cc0;
  }
  * { margin: 0; padding: 0; box-sizing: border-box; }
  html, body {
    width: 1200px; height: 900px; overflow: hidden;
    background: var(--page-bg);
    font-family: "Roboto", Arial, sans-serif;
  }
  .canvas {
    width: 1200px; height: 900px;
    display: flex; flex-direction: column;
    align-items: center; justify-content: center; gap: 36px;
  }
  .card {
    width: 700px; height: 400px;
    background: linear-gradient(135deg, var(--card-bg), var(--card-edge));
    position: relative;
  }
  .card-front {
    display: flex; align-items: center; justify-content: center;
  }
  .wordmark {
    display: flex; align-items: center; gap: 14px;
    color: var(--logo-silver);
    font-weight: 500; letter-spacing: 0.22em; text-transform: uppercase;
    white-space: nowrap;
  }
  .wordmark-dot {
    width: 12px; height: 12px; border-radius: 50%;
    background: var(--logo-silver);
  }
  .card-front .wordmark { font-size: 40px; }
  .card-back .wordmark { font-size: 20px; color: var(--text-white); gap: 10px; }
  .card-back .wordmark-dot { width: 8px; height: 8px; background: var(--text-white); }
  .card-back .brand-side {
    position: absolute; left: 0; top: 0; width: 330px; height: 100%;
    display: flex; align-items: center; justify-content: center;
  }
  .divider {
    position: absolute; left: 335px; top: 125px;
    width: 2px; height: 165px; background: var(--accent-blue);
  }
  .contact {
    position: absolute; left: 360px; top: 125px;
    color: var(--text-white);
    white-space: nowrap;
  }
  .contact-name {
    font-size: 28px; font-weight: 500; letter-spacing: 0.04em;
    color: var(--accent-blue); text-transform: uppercase; margin-bottom: 10px;
  }
  .contact-address { font-size: 16px; line-height: 1.35; margin-bottom: 10px; }
  .contact-line {
    display: flex; align-items: center; gap: 8px;
    font-size: 16px; line-height: 1.5;
  }
  .contact-line svg { width: 13px; height: 13px; flex: none; }
</style>
</head>
<body>
<main class="canvas">
  <section class="card card-front">
    <div class="wordmark"><span>Brightwave</span><span class="wordmark-dot"></span></div>
  </section>

  <section class="card card-back">
    <div class="brand-side">
      <div class="wordmark"><span>Brightwave</span><span class="wordmark-dot"></span></div>
    </div>
    <div class="divider"></div>
    <div class="contact">
      <h1 class="contact-name">Daniel Hartwell</h1>
      <p class="contact-address">318 Harbor Street,<br>Portland, ME 04101</p>
      <p class="contact-line">
        <svg viewBox="0 0 16 16" fill="var(--accent-blue)"><path d="M3.6 1.2l2.3 2.6-1.3 1.6c.9 2 2.5 3.6 4.5 4.5l1.6-1.3 2.6 2.3-1.2 2.2C7 13 3 9 1.4 2.4z"/></svg>
        <span>+1 (555) 014-2276</span>
      </p>
      <p class="contact-line">
        <svg viewBox="0 0 16 16" fill="none" stroke="var(--accent-blue)" stroke-width="1.5"><rect x="1.5" y="3.5" width="13" height="9"/><path d="M1.5 3.5l6.5 5 6.5-5"/></svg>
        <span>daniel.hartwell@brightwave-energy.com</span>
      </p>
      <p class="contact-line">
        <svg viewBox="0 0 16 16" fill="none" stroke="var(--accent-blue)" stroke-width="1.3"><circle cx="8" cy="8" r="6.5"/><ellipse cx="8" cy="8" rx="3" ry="6.5"/><path d="M1.5 8h13"/></svg>
        <span>www.brightwave-energy.com</span>
      </p>
    </div>
  </section>
</main>
</body>
</html>
```